VERUSO - PIZZA - RESTAURANT PIZZERIA

Flyer format:
- A5 front / back leaflet (Example attachment)
Customer logos:
- Attachment, VERUSO PIZZA logo
Address and contact to put on the flyers:
- Phone to add: (+352) 26 58 07 31 (Page 1)
- Address to be added: 8 rue des tilleuls, L-3592 Kayl, Luxembourg (Page 1)
- Website: www.veruso-example.lu (Page 1)
- Leave a space for the timetable (last page)
Flyer color:
- Preferably black background with colored customer logo
Typefaces:
- At your convenience
Descriptions:
- We would like to have a flyer to the one we have put as an example in the attachment
Important elements:
- Pizza oven on the cover page with customer logo, address and contact details
- The graphic elements must be usable and non-paying, we want a quality visual.
- Menu (attachment) The menu is in Word format, it must be laid out in a thoughtful way as on the example model.
- We need to find some pizza and/or ingredient visuals
Aspects :
- The design of the set must be elegant, sober and must contain all the information (Menu, visual of your choice, logo)

Target Market(s)

Private and professional public

Font styles to use
Serif
Sans Serif

Requirements
Must have
• Elegance, take into account the information of the comment
Nice to have
• Pizza oven, Dominant color black, Gold, red
Should not have
• poor quality visuals

```html
<!DOCTYPE html>
<html lang="fr">
<head>
<meta charset="utf-8">
<title>Veruso Pizza – Restaurant Pizzeria</title>
<link href="https://fonts.googleapis.com/css2?family=Oswald:wght@500;600;700&family=Montserrat:wght@400;600;700&display=swap" rel="stylesheet">
<style>
:root{
  --page:#ececec;
  --ink:#0a0a0a;
  --gold:#e2b33c;
  --gold-deep:#b8891f;
  --white:#ffffff;
  --soft:#d6d6d6;
  --ember:#c4521a;
  --ember-dark:#3a1206;
  --crust:#c98a3a;
}
*{box-sizing:border-box;margin:0;padding:0}
html,body{width:1200px;height:3000px;overflow:hidden}
body{
  background:var(--page);
  font-family:"Montserrat",Arial,sans-serif;
  color:var(--white);
  display:flex;flex-direction:column;align-items:center;justify-content:center;gap:60px;
}
.spread{
  width:1120px;height:790px;background:var(--ink);
  display:grid;grid-template-columns:1fr 1fr;position:relative;overflow:hidden;
  box-shadow:0 10px 30px rgba(0,0,0,.18);
}
.half{position:relative;height:100%}

/* shared */
.banner{
  position:relative;background:var(--gold);color:var(--ink);
  font-family:"Oswald",sans-serif;font-weight:600;text-transform:uppercase;
  text-align:center;height:32px;line-height:32px;font-size:19px;letter-spacing:.3px;
  clip-path:polygon(12px 0,calc(100% - 12px) 0,100% 50%,calc(100% - 12px) 100%,12px 100%,0 50%);
}
.banner::after{
  content:"";position:absolute;inset:4px 10px;border-top:1px solid var(--ink);border-bottom:1px solid var(--ink);
}
.banner.small{font-size:15px;height:28px;line-height:28px}
.gold{color:var(--gold)}
.logo{
  font-family:"Oswald",sans-serif;font-weight:600;color:var(--gold);
  letter-spacing:3px;text-transform:uppercase;line-height:1;
}
.icon{width:13px;height:13px;fill:var(--gold);flex:none}
.contact-line{display:flex;align-items:center;gap:8px;font-size:13px}

/* outer left */
.hero-pizza{
  position:absolute;left:60px;top:0;width:420px;height:300px;
  border-radius:0 0 210px 210px;
  background:radial-gradient(circle at 50% 30%,#d9462b 0,#c87a2e 38%,#8f5321 62%,#3b2414 78%,#1a120c 100%);
}
.supplements{position:absolute;left:100px;top:330px;width:340px}
.supp-cols{position:absolute;left:36px;right:36px;top:384px;display:grid;grid-template-columns:1fr 1fr;gap:36px}
.col-title{font-weight:700;font-size:12px;color:var(--gold);text-transform:uppercase;margin-bottom:10px}
.price-list{list-style:none}
.price-list li{
  display:flex;justify-content:space-between;font-size:10px;font-weight:700;
  text-transform:uppercase;padding:5px 0;
}
.price-list .spacer{visibility:hidden}
.outer-foot{position:absolute;left:36px;right:36px;bottom:48px;display:flex;align-items:center;gap:40px}
.outer-foot .logo{font-size:30px}
.outer-foot .contacts{display:flex;flex-direction:column;gap:6px}

/* outer right */
.cover-logo{position:absolute;top:40px;left:150px;font-size:40px}
.oven{
  position:absolute;left:60px;right:0;top:110px;height:320px;
  border-radius:220px 220px 0 0;
  background:
    radial-gradient(ellipse at 50% 78%,#c98a3a 0,#9a5b24 22%,transparent 40%),
    radial-gradient(ellipse at 55% 35%,#ffb347 0,#e8661e 25%,var(--ember) 45%,var(--ember-dark) 75%,var(--ink) 100%);
}
.cover-text{position:absolute;left:60px;right:0;top:440px;text-align:center}
.welcome{font-weight:700;font-size:18px}
.restaurant{font-family:"Oswald",sans-serif;font-weight:600;font-size:54px;line-height:1.05;letter-spacing:1px}
.pizzeria{font-family:"Oswald",sans-serif;font-weight:700;font-size:88px;line-height:1;color:var(--gold);letter-spacing:1px}
.gold-bar{width:70px;height:6px;border-radius:3px;background:var(--gold);margin:12px auto 0}
.rule{height:1px;background:#4a4a4a;margin:8px 30px 0}
.cover-contacts{margin-top:14px;display:flex;flex-direction:column;align-items:center;gap:10px}
.cover-contacts .row{display:flex;gap:10px;align-items:center;font-size:13px}

/* inner left */
.inner-left{padding:22px 30px 22px 30px;display:flex;flex-direction:column}
.banner-wrap{position:relative;width:300px;margin:0 auto}
.banner-badge{
  position:absolute;top:50%;width:40px;height:40px;margin-top:-20px;border-radius:50%;
  background:radial-gradient(circle,#d9462b 0,#c98a3a 55%,#8a4e1c 100%);
}
.banner-badge.l{left:-22px}.banner-badge.r{right:-22px}
.banner-mark{
  position:absolute;top:50%;width:22px;height:22px;margin-top:-11px;background:var(--gold);
  clip-path:polygon(0 0,100% 50%,0 100%);
}
.banner-mark.l{left:-32px}.banner-mark.r{right:-32px;transform:scaleX(-1)}
.pizza-cols{display:grid;grid-template-columns:1fr 1fr;column-gap:26px;margin:14px 0 16px}
.pizza-col{display:flex;flex-direction:column;gap:7px}
.item-head{display:flex;justify-content:space-between;font-size:10px;font-weight:700;text-transform:uppercase}
.item-desc{font-size:9px;line-height:1.2;color:var(--soft);max-width:170px}

/* inner right */
.inner-right{padding:22px 26px 0 16px;display:grid;grid-template-columns:1fr 1fr;column-gap:18px}
.stack{display:flex;flex-direction:column}
.panini{display:grid;grid-template-columns:1fr 1fr;column-gap:14px;row-gap:4px;margin:12px 0 22px}
.panini .item-head{font-size:10px}
.salads{display:flex;flex-direction:column;gap:7px;margin:12px 0 22px}
.desserts{list-style:none;margin:12px 0 18px}
.desserts li{display:flex;justify-content:space-between;font-size:10px;font-weight:700;text-transform:uppercase;padding:4px 0}
.drinks{
  border:1px solid #8a8a8a;border-radius:4px;padding:5px;
}
.drinks-inner{
  border:1px solid #8a8a8a;border-radius:3px;padding:12px 8px;text-align:center;
  font-size:9px;font-weight:700;text-transform:uppercase;line-height:1.35;display:flex;flex-direction:column;gap:9px;
}
.pates{margin-top:12px}
.pates .col-title{margin-bottom:4px}
.pates ul{list-style:none;margin-bottom:8px}
.pates li{display:flex;align-items:baseline;gap:4px;font-size:9.5px;font-weight:700;text-transform:uppercase;padding:2px 0}
.pates li .dots{flex:1;border-bottom:1px dotted #9a9a9a}
.pates li.plain .dots{border:none}
.details{
  border:1px solid var(--gold);border-radius:3px;padding:14px 10px;margin-top:8px;
  color:var(--gold);font-size:9.5px;font-weight:700;text-transform:uppercase;text-align:center;line-height:1.35;
  display:flex;flex-direction:column;gap:12px;
}
.slice-photo{
  position:absolute;right:0;bottom:0;width:280px;height:230px;border-radius:140px 0 0 0;
  background:radial-gradient(circle at 60% 60%,#d9462b 0,#e0a24a 35%,#b36b2a 60%,#3a2414 85%,var(--ink) 100%);
}
</style>
</head>
<body>

<!-- Outer spread: back page + cover -->
<section class="spread outer">
  <div class="half outer-left">
    <div class="hero-pizza" role="img" aria-label="Photo d'une pizza aux tomates, olives, salami et basilic vue de dessus"></div>
    <div class="banner supplements">Supplements</div>
    <div class="supp-cols">
      <div>
        <h3 class="col-title">Spaghetti</h3>
        <ul class="price-list">
          <li><span>Legumes</span><span></span></li>
          <li><span>Mozza</span><span>1,50€</span></li>
          <li><span>Poivron</span><span>1,50€</span></li>
          <li><span>Burrata</span><span>3,50€</span></li>
          <li><span>Champignon</span><span>2€</span></li>
          <li><span>Buffala</span><span>5€</span></li>
          <li><span>Oignon</span><span>1,50€</span></li>
          <li><span>Chevre</span><span>2€</span></li>
          <li><span>Pomme de terre</span><span>2€</span></li>
          <li><span>St nectaire</span><span>2,50€</span></li>
          <li><span>Aubergine</span><span>2€</span></li>
        </ul>
      </div>
      <div>
        <h3 class="col-title">Viandes</h3>
        <ul class="price-list">
          <li class="spacer"><span>-</span></li>
          <li><span>Legumes</span><span></span></li>
          <li><span>Poulet</span><span>2,50€</span></li>
          <li><span>Viande hachee</span><span>2,50€</span></li>
          <li><span>Merguez</span><span>2,50€</span></li>
          <li><span>Câpre</span><span>1,50€</span></li>
          <li><span>Jambon cuit</span><span>2€</span></li>
          <li><span>Ail</span><span>1€</span></li>
          <li><span>Lardon</span><span>2€</span></li>
          <li><span>Olive</span><span>1€</span></li>
        </ul>
      </div>
    </div>
    <div class="outer-foot">
      <div class="logo">Veruso<br>Pizza</div>
      <div class="contacts">
        <div class="contact-line"><svg class="icon" viewBox="0 0 24 24"><path d="M6.6 10.8a15.2 15.2 0 0 0 6.6 6.6l2.2-2.2c.3-.3.7-.4 1-.2 1.1.4 2.3.6 3.6.6.6 0 1 .4 1 1V20c0 .6-.4 1-1 1A17 17 0 0 1 3 4c0-.6.4-1 1-1h3.5c.6 0 1 .4 1 1 0 1.3.2 2.5.6 3.6.1.3 0 .7-.2 1z"/></svg>(+352) 26 58 07 31</div>
        <div class="contact-line"><svg class="icon" viewBox="0 0 24 24"><path d="M12 2a7 7 0 0 0-7 7c0 5.2 7 13 7 13s7-7.8 7-13a7 7 0 0 0-7-7zm0 9.5A2.5 2.5 0 1 1 12 6.5a2.5 2.5 0 0 1 0 5z"/></svg>8 rue des tilleuls, L-3592 Kayl,<br>Luxembourg</div>
        <div class="contact-line"><svg class="icon" viewBox="0 0 24 24"><path d="M12 2a10 10 0 1 0 0 20 10 10 0 0 0 0-20zm6.9 6h-3a15.7 15.7 0 0 0-1.4-3.6A8 8 0 0 1 18.9 8zM12 4c.8 1.2 1.5 2.5 1.9 4h-3.8c.4-1.5 1.1-2.8 1.9-4zM4.3 14a8 8 0 0 1 0-4h3.4a16.5 16.5 0 0 0 0 4zm.8 2h3a15.7 15.7 0 0 0 1.4 3.6A8 8 0 0 1 5.1 16zm3-8h-3a8 8 0 0 1 4.4-3.6C8.9 5.5 8.4 6.7 8.1 8zM12 20c-.8-1.2-1.5-2.5-1.9-4h3.8c-.4 1.5-1.1 2.8-1.9 4zm2.3-6H9.7a14.7 14.7 0 0 1 0-4h4.6a14.7 14.7 0 0 1 0 4zm.3 5.6c.6-1.1 1.1-2.3 1.4-3.6h3a8 8 0 0 1-4.4 3.6zm1.7-5.6a16.5 16.5 0 0 0 0-4h3.4a8 8 0 0 1 0 4z"/></svg>www.veruso-example.lu</div>
      </div>
    </div>
  </div>

  <div class="half outer-right">
    <div class="oven" role="img" aria-label="Photo d'un four à bois en flammes avec une pizza posée devant"></div>
    <div class="logo cover-logo">Veruso Pizza</div>
    <div class="cover-text">
      <p class="welcome">Welcome to Veruso pizza</p>
      <h1 class="restaurant">RESTAURANT</h1>
      <h2 class="pizzeria">PIZZERIA</h2>
      <div class="gold-bar"></div>
      <div class="rule"></div>
      <div class="cover-contacts">
        <div class="row">
          <span class="contact-line"><svg class="icon" viewBox="0 0 24 24"><path d="M6.6 10.8a15.2 15.2 0 0 0 6.6 6.6l2.2-2.2c.3-.3.7-.4 1-.2 1.1.4 2.3.6 3.6.6.6 0 1 .4 1 1V20c0 .6-.4 1-1 1A17 17 0 0 1 3 4c0-.6.4-1 1-1h3.5c.6 0 1 .4 1 1 0 1.3.2 2.5.6 3.6.1.3 0 .7-.2 1z"/></svg>(+352) 26 58 07 31</span>
          <span>|</span>
          <span class="contact-line"><svg class="icon" viewBox="0 0 24 24"><circle cx="12" cy="12" r="9" fill="none" stroke="currentColor"/><path d="M12 2a10 10 0 1 0 0 20 10 10 0 0 0 0-20zm0 2c.8 1.2 1.5 2.5 1.9 4h-3.8c.4-1.5 1.1-2.8 1.9-4zm-7.7 10a8 8 0 0 1 0-4h3.4a16.5 16.5 0 0 0 0 4zm7.7 6c-.8-1.2-1.5-2.5-1.9-4h3.8c-.4 1.5-1.1 2.8-1.9 4zm2.3-6H9.7a14.7 14.7 0 0 1 0-4h4.6a14.7 14.7 0 0 1 0 4zm2-0a16.5 16.5 0 0 0 0-4h3.4a8 8 0 0 1 0 4z"/></svg>www.veruso-example.lu</span>
        </div>
        <div class="contact-line"><svg class="icon" viewBox="0 0 24 24"><path d="M12 2a7 7 0 0 0-7 7c0 5.2 7 13 7 13s7-7.8 7-13a7 7 0 0 0-7-7zm0 9.5A2.5 2.5 0 1 1 12 6.5a2.5 2.5 0 0 1 0 5z"/></svg>8 rue des tilleuls, L-3592 Kayl, Luxembourg</div>
      </div>
    </div>
  </div>
</section>

<!-- Inner spread: menu -->
<section class="spread inner">
  <div class="half inner-left">
    <div class="banner-wrap">
      <span class="banner-badge l" role="img" aria-label="Petite photo de pizza"></span>
      <div class="banner">Pizza: base tomate</div>
      <span class="banner-badge r" role="img" aria-label="Petite photo de pizza"></span>
    </div>
    <div class="pizza-cols">
      <div class="pizza-col">
        <div><div class="item-head"><span>Marinara</span><span>15€</span></div><p class="item-desc">Anchois,capres,olive,ail</p></div>
        <div><div class="item-head"><span>Napolitaine</span><span>9,50€</span></div><p class="item-desc">Ail origan</p></div>
        <div><div class="item-head"><span>Margharita</span><span>10€</span></div><p class="item-desc">Mozza</p></div>
        <div><div class="item-head"><span>4 Fromages</span><span>14,50€</span></div><p class="item-desc">Mozza,chevre,<br>parmesan,gorgonzola</p></div>
        <div><div class="item-head"><span>Chevre</span><span>15€</span></div><p class="item-desc">Mozza,jambon cuit,<br>chevre,olive</p></div>
        <div><div class="item-head"><span>Chorizo</span><span>15€</span></div><p class="item-desc">Mozza, chorizo,<br>poivrons,olive</p></div>
        <div><div class="item-head"><span>Vegetarienne</span><span>15€</span></div><p class="item-desc">Mozza, cougette,<br>olive, poivrons, aubergine</p></div>
        <div><div class="item-head"><span>3Viandes</span><span>17,50€</span></div><p class="item-desc">Mozza,vianche haché,<br>merguez,poulet,poivrons,oeuf</p></div>
        <div><div class="item-head"><span>Buffala</span><span>15€</span></div><p class="item-desc">Mozza,buffala</p></div>
        <div><div class="item-head"><span>Calzone jambon</span><span>14,50€</span></div><p class="item-desc">Mozza,jambon cuit,<br>champignon</p></div>
      </div>
      <div class="pizza-col">
        <div><div class="item-head"><span>Calzone chorizo</span><span>14,50€</span></div><p class="item-desc">Mozza,chorizo,riccota</p></div>
        <div><div class="item-head"><span>Bambino</span><span>13€</span></div><p class="item-desc">Mozza,jambon,olive</p></div>
        <div><div class="item-head"><span>Reine</span><span>14€</span></div><p class="item-desc">Mozza, jambon,champignon</p></div>
        <div><div class="item-head"><span>Neptune</span><span>14,50€</span></div><p class="item-desc">Mozza,thon,oignon,olive</p></div>
        <div><div class="item-head"><span>Poulet</span><span>17€</span></div><p class="item-desc">Mozza,poulet,poivron,<br>oignon,champignon,olive</p></div>
        <div><div class="item-head"><span>Campagnarde</span><span>15€</span></div><p class="item-desc">Mozza,jambon,artichaud<br>champignon,oeuf</p></div>
        <div><div class="item-head"><span>Mediterranienne</span><span>17,50€</span></div><p class="item-desc">Mozza,fruits de mer</p></div>
        <div><div class="item-head"><span>Exotique</span><span>16,50€</span></div><p class="item-desc">Mozza,poulet,chevre,ananas</p></div>
        <div><div class="item-head"><span>4 Saisons</span><span>14,50€</span></div><p class="item-desc">Mozza,champignon,artichaud<br>jambon cuits, olive</p></div>
        <div><div class="item-head"><span>Scampi</span><span>14,50€</span></div><p class="item-desc">Mozza, ail, origan, scampi</p></div>
        <div><div class="item-head"><span>Veruso</span><span>18€</span></div><p class="item-desc">Mozza, porcini,chorizo,<br>mozza fumé</p></div>
      </div>
    </div>
    <div class="banner-wrap">
      <span class="banner-mark l"></span>
      <div class="banner">Pizza: base crème</div>
      <span class="banner-mark r"></span>
    </div>
    <div class="pizza-cols">
      <div class="pizza-col">
        <div><div class="item-head"><span>Bianca</span><span>12,50€</span></div><p class="item-desc">mozza,jambon</p></div>
        <div><div class="item-head"><span>Chèvre miel</span><span>13€</span></div><p class="item-desc">mozza chevre frais miel</p></div>
        <div><div class="item-head"><span>Umberto</span><span>14,50€</span></div><p class="item-desc">creme gorgonzola parmesan</p></div>
        <div><div class="item-head"><span>Fermiere</span><span>16€</span></div><p class="item-desc">mozza,poulet,champignon,<br>oignon</p></div>
        <div><div class="item-head"><span>Gorgonzola</span><span>16,50€</span></div><p class="item-desc">mozza,lardon,oignon,<br>gorgonzola,st nectaire,chevre</p></div>
      </div>
      <div class="pizza-col">
        <div><div class="item-head"><span>Moselle</span><span>16,50€</span></div><p class="item-desc">mozza,viande hachée,lardon,pomme</p></div>
        <div><div class="item-head"><span>Bauca neve</span><span>15,50€</span></div><p class="item-desc">mozza,burrata,andouillette</p></div>
        <div><div class="item-head"><span>Raquette:</span><span>20,50€</span></div><p class="item-desc">mozza,riccota,jambon cuit,jambon<br>cru,tomate cerise,parmesan</p></div>
        <div><div class="item-head"><span>Mortadela</span><span>14,50€</span></div><p class="item-desc">mozza burrata,pistache</p></div>
        <div><div class="item-head"><span>Parma</span><span>17€</span></div><p class="item-desc">mozza,tomate cerise,roquette,<br>parmesan,jambon de parme</p></div>
      </div>
    </div>
  </div>

  <div class="half inner-right">
    <div class="stack">
      <div class="banner small">Panini base creme + mozza</div>
      <div class="panini">
        <div class="item-head"><span>4Fromages</span><span>7€</span></div>
        <div class="item-head"><span>Poulet</span><span>7€</span></div>
        <div class="item-head"><span>Saumon</span><span>7€</span></div>
        <div class="item-head"><span>Jambon</span><span>7€</span></div>
        <div class="item-head"><span>Merguez</span><span>7€</span></div>
        <div class="item-head"><span>Viande hachée</span><span>7€</span></div>
      </div>
      <div class="banner small">Salades</div>
      <div class="salads">
        <div><div class="item-head"><span>Nicoise</span><span>15,50€</span></div><p class="item-desc">tomate, thon,olive,pomme de terre</p></div>
        <div><div class="item-head"><span>Norvegienne</span><span>16€</span></div><p class="item-desc">tomate, saumon,oignon</p></div>
        <div><div class="item-head"><span>Chevre chaud</span><span>16€</span></div><p class="item-desc">tomate lardon, chevre sur toast</p></div>
        <div><div class="item-head"><span>Jambon:</span><span>16€</span></div><p class="item-desc">jambon, roquette, parmesan</p></div>
      </div>
      <div class="banner small">Desserts</div>
      <ul class="desserts">
        <li><span>Mousse au chocolat</span><span>7€</span></li>
        <li><span>Tiramisu: classique, nocciola</span><span>7€</span></li>
        <li><span>Baba au rhum</span><span>8€</span></li>
        <li><span>Crème brulé</span><span>6,50€</span></li>
        <li><span>Café : expresso</span><span>1,80€ &nbsp;Thé : 1,50€</span></li>
        <li><span>Capuccino</span><span>2,20€</span></li>
      </ul>
      <div class="drinks">
        <div class="drinks-inner">
          <p>Boissons 33cl: &nbsp; 2,50€</p>
          <p>Cola Nera, Cola Nera zero, Cola Nera<br>cherry, Aranca, Limeo, Sunjus,<br>eau, Teavio, Oazo</p>
          <p>Boissons bouteille: &nbsp; 5,50 €</p>
          <p>Cola Nera, Aranca,<br>Fonte Rivo, Teavio</p>
          <p>Alcools et vin: ??????????</p>
        </div>
      </div>
    </div>
    <div class="stack">
      <div class="banner small">Pates</div>
      <div class="pates">
        <h3 class="col-title">Spaghetti</h3>
        <ul>
          <li class="plain"><span>Tagliatelle</span><span class="dots"></span></li>
          <li><span>Carbonnara</span><span class="dots"></span><span>14€</span></li>
          <li><span>Carbonnara</span><span class="dots"></span><span>14€</span></li>
          <li><span>Bolognaise</span><span class="dots"></span><span>14€</span></li>
          <li><span>Bolognaise</span><span class="dots"></span><span>14€</span></li>
          <li><span>Ariabata</span><span class="dots"></span><span>13€</span></li>
          <li><span>Ariabata</span><span class="dots"></span><span>13€</span></li>
          <li><span>Ati</span><span class="dots"></span><span>18€</span></li>
          <li><span>Ati</span><span class="dots"></span><span>18€</span></li>
          <li><span>Saumon</span><span class="dots"></span><span>17€</span></li>
          <li><span>Saumon</span><span class="dots"></span><span>17€</span></li>
        </ul>
        <h3 class="col-title">Penne</h3>
        <ul>
          <li><span>Carbonnara</span><span class="dots"></span><span>14€</span></li>
          <li><span>Bolognaise</span><span class="dots"></span><span>14€</span></li>
          <li><span>Ariabata</span><span class="dots"></span><span>13€</span></li>
          <li><span>Ati</span><span class="dots"></span><span>18€</span></li>
          <li><span>Saumon</span><span class="dots"></span><span>17€</span></li>
        </ul>
        <div class="details">
          <p>Details : - Ati porcini, horizo,<br>mozza fumee</p>
          <p>Saumon : creme, saumon,<br>oignon</p>
          <p>Lasagne maison 14,50€</p>
        </div>
      </div>
    </div>
    <div class="slice-photo" role="img" aria-label="Photo d'une pizza garnie avec une part retirée"></div>
  </div>
</section>

</body>
</html>
```